Lantern: Social Media Image: FLU

We are looking to create a social media graphic that can be used. We would like it to mimic this --> https://www.tolvara.org/Roll-up-today_01.png
Will contain the:
-- Campaign Name: LANTERN,
-- Moto: Protect Your Community. Protect Your Elders. Stay Vaccinated.
-- QB5 logo
-- Language: Learn more about getting vaccinated against COVID-19
-- Picture of real person

Please reference our QB5 homepage for visual inspiration qbquintet.org or look here: https://qbquintet.org/resources/memory-care-handouts-strong-body-strong-mind/

```html
<!DOCTYPE html>
<html lang="en">
<head>
<meta charset="utf-8">
<title>Lantern – Stay Vaccinated</title>
<link rel="stylesheet" href="https://fonts.googleapis.com/css2?family=Saira+Stencil+One&family=Questrial&family=Roboto+Condensed:wght@700&display=swap">
<style>
  :root {
    --parchment-light: #f3e7c8;
    --parchment: #e9d6a7;
    --parchment-deep: #d8bd82;
    --sepia-light: #e2c58d;
    --sepia: #c9a263;
    --sepia-deep: #a47940;
    --sepia-dark: #6e4a26;
    --brown: #7a3a2c;
    --frame: #a45a36;
    --rose: #a85762;
    --wine: #843d40;
    --orange: #c8501c;
    --band: #9a7431;
    --teal: #2e8a72;
    --white: #fbf6ea;
  }
  * { margin: 0; padding: 0; box-sizing: border-box; }
  html, body { width: 927px; height: 1200px; overflow: hidden; }
  body { background: var(--parchment); }
  .poster {
    position: relative;
    width: 927px;
    height: 1200px;
    overflow: hidden;
    background:
      linear-gradient(90deg, rgba(216,189,130,0) 88%, rgba(214,178,104,0.55) 100%),
      radial-gradient(ellipse at 65% 45%, var(--parchment-light) 0%, var(--parchment) 60%, var(--parchment-deep) 100%);
    font-family: "Questrial", sans-serif;
  }
  .portrait {
    position: absolute;
    left: 0; top: 110px;
    width: 470px; height: 870px;
    background:
      radial-gradient(ellipse 70% 55% at 30% 55%, var(--sepia-light) 0%, rgba(226,197,141,0) 70%),
      radial-gradient(ellipse 60% 40% at 15% 92%, var(--sepia-dark) 0%, rgba(110,74,38,0) 75%),
      linear-gradient(160deg, var(--sepia) 0%, var(--sepia-deep) 55%, var(--sepia) 100%);
    -webkit-mask-image: linear-gradient(90deg, #000 72%, transparent 100%), linear-gradient(180deg, transparent 0%, #000 14%, #000 84%, transparent 100%);
    -webkit-mask-composite: source-in;
    mask-image: linear-gradient(90deg, #000 72%, transparent 100%), linear-gradient(180deg, transparent 0%, #000 14%, #000 84%, transparent 100%);
    mask-composite: intersect;
  }
  .campaign-frame { position: absolute; left: 400px; top: 0; width: 404px; height: 130px; }
  .campaign-name {
    position: absolute; left: 444px; top: 22px;
    font-family: "Saira Stencil One", sans-serif;
  }
  .motto { position: absolute; left: 467px; top: 300px; width: 440px; height: 480px; }
  .motto-lead {
    display: block;
    font-size: 50px;
    line-height: 1;
    color: var(--rose);
  }
  .motto svg { display: block; font-family: "Saira Stencil One", sans-serif; }
  .lead-community { position: absolute; top: 0; }
  .word-community { position: absolute; top: 64px; }
  .lead-elders { position: absolute; top: 165px; }
  .word-elders { position: absolute; top: 231px; }
  .lead-stay { position: absolute; top: 343px; }
  .word-vaccinated { position: absolute; top: 419px; }
  .org {
    position: absolute; left: 469px; top: 832px;
    display: flex; align-items: center; gap: 16px;
    font-family: "Roboto Condensed", sans-serif;
    font-weight: 700;
    color: var(--teal);
  }
  .org-mark { width: 60px; height: 60px; background: var(--teal); }
  .org-divider { width: 2px; height: 68px; background: var(--teal); }
  .org-name { font-size: 25px; line-height: 1.15; letter-spacing: 0.2px; }
  .info-band {
    position: absolute; left: 0; top: 1049px;
    width: 927px; height: 80px;
    background: var(--band);
    display: flex; align-items: center;
    padding-left: 116px;
  }
  .info-band p { color: var(--white); font-size: 27px; letter-spacing: 0.3px; }
</style>
</head>
<body>
<main class="poster">
  <div class="portrait" role="img" aria-label="Sepia portrait of a smiling elder, close-up, filling the left side"></div>

  <svg class="campaign-frame" viewBox="0 0 404 130" aria-hidden="true">
    <g fill="none" stroke="var(--frame)" stroke-width="6">
      <polyline points="3,0 3,120 266,120"/>
      <polyline points="398,0 398,124"/>
    </g>
    <g fill="var(--frame)">
      <polygon points="283,108 308,120 283,132"/>
      <polygon points="313,108 338,120 313,132"/>
      <polygon points="343,108 368,120 343,132"/>
    </g>
  </svg>
  <svg class="campaign-name" width="320" height="60" viewBox="0 0 320 60">
    <text x="0" y="54" font-size="64" fill="var(--brown)" textLength="317" lengthAdjust="spacingAndGlyphs">LANTERN</text>
  </svg>

  <section class="motto">
    <span class="motto-lead lead-community">Protect Your</span>
    <svg class="word-community" width="440" height="62" viewBox="0 0 440 62">
      <text x="0" y="58" font-size="72" fill="var(--wine)" textLength="435" lengthAdjust="spacingAndGlyphs">COMMUNITY</text>
    </svg>
    <span class="motto-lead lead-elders">Protect Your</span>
    <svg class="word-elders" width="292" height="62" viewBox="0 0 292 62">
      <text x="0" y="58" font-size="72" fill="var(--wine)" textLength="290" lengthAdjust="spacingAndGlyphs">ELDERS</text>
    </svg>
    <span class="motto-lead lead-stay">Stay</span>
    <svg class="word-vaccinated" width="440" height="60" viewBox="0 0 440 60">
      <text x="0" y="56" font-size="70" fill="var(--orange)" textLength="430" lengthAdjust="spacingAndGlyphs">VACCINATED</text>
    </svg>
  </section>

  <div class="org">
    <span class="org-mark" aria-hidden="true"></span>
    <span class="org-divider" aria-hidden="true"></span>
    <p class="org-name">QB5 QUINTET BUREAU FOR<br>ELDER WELLBEING</p>
  </div>

  <div class="info-band">
    <p>Learn more about getting vaccinated against COVID-19</p>
  </div>
</main>
</body>
</html>
```